Business cards

I would like a black background with the design I previously chose. I need 2 sets of cards. Mine will have Marisol Brandt, Broker/Owner, 307-555-0148 and marisol.harborpeak@mailvista.com
The second set will read, Dana Rutledge, Realtor 307-555-0172, dana.harborpeak@mailvista.com

Industry/Entity Type

Business

```html
<!DOCTYPE html>
<html lang="en">
<head>
<meta charset="UTF-8">
<title>Harbor Peak Business Cards</title>
<link rel="stylesheet" href="https://fonts.googleapis.com/css2?family=Josefin+Sans:wght@300;400&family=Marcellus&display=swap">
<style>
  :root {
    --page: #ffffff;
    --card: #0d0d0d;
    --card-glow: #222222;
    --silver: #c9c6bb;
    --text-light: #e2e2e2;
    --text-muted: #bdbdbd;
    --icon: #d8d8d8;
  }
  * { margin: 0; padding: 0; box-sizing: border-box; }
  html, body {
    width: 1200px;
    height: 1200px;
    overflow: hidden;
    background: var(--page);
  }
  .sheet {
    position: relative;
    width: 1200px;
    height: 1200px;
  }
  .card {
    position: absolute;
    top: 492px;
    width: 362px;
    height: 215px;
    background: var(--card);
    overflow: hidden;
    font-family: "Josefin Sans", sans-serif;
  }
  .card--broker { left: 224px; }
  .card--realtor { left: 615px; }
  .card__texture {
    position: absolute;
    inset: 0;
    background:
      radial-gradient(ellipse at 30% 20%, var(--card-glow) 0%, transparent 55%),
      radial-gradient(ellipse at 80% 85%, #1a1a1a 0%, transparent 50%),
      linear-gradient(135deg, #141414 0%, #080808 60%, #121212 100%);
  }
  .wordmark {
    position: absolute;
    left: 12px;
    top: 58px;
    width: 146px;
    text-align: center;
    color: var(--silver);
    font-family: "Josefin Sans", sans-serif;
    font-weight: 400;
    line-height: 1;
  }
  .wordmark__name {
    display: block;
    font-size: 15px;
    letter-spacing: 0.5px;
    text-transform: uppercase;
  }
  .wordmark__sub {
    display: block;
    margin-top: 4px;
    font-size: 5px;
    letter-spacing: 1.6px;
    text-transform: uppercase;
  }
  .wordmark__rule {
    display: block;
    margin: 4px auto 0;
    width: 130px;
    height: 1px;
    background: var(--silver);
  }
  .person {
    position: absolute;
    top: 56px;
    left: 170px;
    width: 146px;
    text-align: center;
  }
  .person__name {
    font-weight: 300;
    font-size: 15.5px;
    color: var(--text-light);
    text-transform: uppercase;
    white-space: nowrap;
    letter-spacing: 0;
    margin-left: -30px;
    margin-right: -30px;
  }
  .person__title {
    margin-top: 1px;
    font-weight: 300;
    font-size: 7.5px;
    letter-spacing: 1.4px;
    color: var(--text-muted);
  }
  .contact {
    position: absolute;
    left: 20px;
    top: 159px;
    list-style: none;
    font-family: "Marcellus", serif;
    font-size: 8.6px;
    color: var(--text-muted);
  }
  .contact__item {
    display: flex;
    align-items: center;
    gap: 5px;
    height: 12px;
  }
  .contact__icon {
    width: 9px;
    height: 9px;
    flex: none;
  }
</style>
</head>
<body>
<main class="sheet">

  <article class="card card--broker">
    <div class="card__texture"></div>
    <div class="wordmark">
      <span class="wordmark__name">Harbor Peak</span>
      <span class="wordmark__sub">Real Estate Group LLC</span>
      <span class="wordmark__rule"></span>
    </div>
    <div class="person">
      <h2 class="person__name">Marisol Brandt</h2>
      <p class="person__title">Broker/Owner</p>
    </div>
    <ul class="contact">
      <li class="contact__item">
        <svg class="contact__icon" viewBox="0 0 10 10" aria-hidden="true">
          <rect x="0" y="0" width="10" height="10" rx="2" fill="var(--icon)"/>
          <rect x="3" y="1.8" width="4" height="6.4" rx="0.8" fill="none" stroke="#111" stroke-width="0.9"/>
        </svg>
        <span>307-555-0148</span>
      </li>
      <li class="contact__item">
        <svg class="contact__icon" viewBox="0 0 10 10" aria-hidden="true">
          <rect x="0" y="0" width="10" height="10" rx="2" fill="var(--icon)"/>
          <circle cx="5" cy="5" r="3" fill="none" stroke="#111" stroke-width="0.9"/>
          <path d="M2 5h6M5 2c1.4 1.6 1.4 4.4 0 6M5 2c-1.4 1.6-1.4 4.4 0 6" fill="none" stroke="#111" stroke-width="0.6"/>
        </svg>
        <span>marisol.harborpeak@mailvista.com</span>
      </li>
    </ul>
  </article>

  <article class="card card--realtor">
    <div class="card__texture"></div>
    <div class="wordmark">
      <span class="wordmark__name">Harbor Peak</span>
      <span class="wordmark__sub">Real Estate Group LLC</span>
      <span class="wordmark__rule"></span>
    </div>
    <div class="person">
      <h2 class="person__name">Dana Rutledge</h2>
      <p class="person__title">Realtor</p>
    </div>
    <ul class="contact">
      <li class="contact__item">
        <svg class="contact__icon" viewBox="0 0 10 10" aria-hidden="true">
          <rect x="0" y="0" width="10" height="10" rx="2" fill="var(--icon)"/>
          <rect x="3" y="1.8" width="4" height="6.4" rx="0.8" fill="none" stroke="#111" stroke-width="0.9"/>
        </svg>
        <span>307-555-0172</span>
      </li>
      <li class="contact__item">
        <svg class="contact__icon" viewBox="0 0 10 10" aria-hidden="true">
          <rect x="0" y="0" width="10" height="10" rx="2" fill="var(--icon)"/>
          <circle cx="5" cy="5" r="3" fill="none" stroke="#111" stroke-width="0.9"/>
          <path d="M2 5h6M5 2c1.4 1.6 1.4 4.4 0 6M5 2c-1.4 1.6-1.4 4.4 0 6" fill="none" stroke="#111" stroke-width="0.6"/>
        </svg>
        <span>dana.harborpeak@mailvista.com</span>
      </li>
    </ul>
  </article>

</main>
</body>
</html>
```